Attention grabbing 6x9 postcard

We are looking to have an attention grabbing post card that be sent out to homeowners from our roofing company Olum Roofing. the concept is that on the front it will say something like (STOP THE KNOCKING!
Tired of roofers knocking on your door? Contact us because we value your time as much as you value the roof over your head."
Olum Roofing
OlumRoofing.com
877.612.OLUM
info@olumroofing.com

Please feel free to come up with something very creative. Once we pick the final design we will provide the copy.

```html
<!DOCTYPE html>
<html lang="en">
<head>
<meta charset="utf-8">
<title>Olum Roofing – Stop the Knocking Postcard</title>
<link rel="stylesheet" href="https://fonts.googleapis.com/css2?family=Archivo:wdth,wght@125,800;125,900&family=Poppins:wght@700;800&display=swap">
<style>
  :root {
    --navy: #28296b;
    --yellow: #f6de0b;
    --yellow-deep: #d8bb2c;
    --yellow-soft: #e9cf43;
    --ink: #0b0b0b;
  }
  * { margin: 0; padding: 0; box-sizing: border-box; }
  html, body { width: 845px; height: 1200px; overflow: hidden; background: var(--navy); }
  .postcard {
    position: relative;
    width: 845px;
    height: 1200px;
    background: var(--navy);
    overflow: hidden;
    font-family: "Poppins", sans-serif;
    color: var(--ink);
  }
  .shapes { position: absolute; inset: 0; }
  .brand {
    position: absolute;
    left: 20px; top: 70px;
    width: 270px;
    text-align: center;
    font-family: "Poppins", sans-serif;
    font-weight: 800;
    font-size: 44px;
    line-height: 1.05;
    color: var(--ink);
  }
  .headline {
    position: absolute;
    left: 385px; top: 636px;
    width: 460px;
    font-family: "Archivo", sans-serif;
    font-stretch: 125%;
    font-weight: 900;
    font-size: 57px;
    line-height: 70px;
    text-transform: uppercase;
    text-align: center;
    letter-spacing: 0.5px;
  }
  .headline .line-two { display: block; margin-left: -14px; }
  .message {
    position: absolute;
    left: 0; top: 845px;
    width: 845px;
    text-align: center;
    font-weight: 700;
    font-size: 25.5px;
    line-height: 38px;
  }
  .info-title {
    position: absolute;
    left: 13px; top: 1074px;
    font-weight: 700;
    font-size: 23px;
    letter-spacing: 0.3px;
  }
  .contact {
    position: absolute;
    display: flex;
    align-items: center;
    gap: 10px;
    font-family: "Archivo", sans-serif;
    font-stretch: 125%;
    font-weight: 800;
    font-size: 15px;
  }
  .contact svg { width: 36px; height: 36px; flex: none; }
  .contact-location { left: 19px; top: 1104px; }
  .contact-phone { left: 351px; top: 1102px; }
  .contact-email { left: 19px; top: 1147px; }
</style>
</head>
<body>
<main class="postcard">
  <svg class="shapes" width="845" height="1200" viewBox="0 0 845 1200" aria-hidden="false">
    <defs>
      <linearGradient id="houseTone" x1="0" y1="0" x2="1" y2="1">
        <stop offset="0" stop-color="#4a4a50"/>
        <stop offset="0.45" stop-color="#b9c2d2"/>
        <stop offset="1" stop-color="#dfe4ec"/>
      </linearGradient>
      <linearGradient id="roofTone" x1="0" y1="0" x2="1" y2="1">
        <stop offset="0" stop-color="#3fb2d8"/>
        <stop offset="0.5" stop-color="#cf9256"/>
        <stop offset="1" stop-color="#4cc3e6"/>
      </linearGradient>
    </defs>
    <path class="brand-panel" d="M0 0 H290 Q318 0 312 40 L262 225 Q248 262 205 270 L70 284 Q30 288 0 255 Z" fill="var(--yellow)"/>
    <path class="photo-house" role="img" aria-label="Aerial photo of a roofer installing shingles on a two-storey white house"
      d="M326 0 H845 V497 L530 536 Q505 539 492 520 L295 265 Q280 245 285 220 Z" fill="url(#houseTone)"/>
    <path class="photo-roof" role="img" aria-label="Aerial photo of a crew laying blue underlayment on a roof deck"
      d="M0 322 L225 299 Q250 297 265 315 L415 495 Q428 512 422 530 L348 738 Q340 758 318 762 L100 795 L0 792 Z" fill="url(#roofTone)"/>
    <path class="headline-band" d="M410 608 H845 V789 H340 Z" fill="var(--yellow)"/>
    <rect class="message-band" x="0" y="818" width="845" height="180" fill="var(--yellow)"/>
    <path class="info-band" d="M0 1061 H743 L845 1200 H0 Z" fill="var(--yellow)"/>
    <path d="M743 1061 L845 1200 H641 Z" fill="var(--yellow-deep)"/>
    <path d="M724 1088 L806 1200 H641 Z" fill="var(--yellow-soft)"/>
  </svg>

  <div class="brand">Olum<br>Roofing</div>

  <h1 class="headline">Stop the <span class="line-two">Knocking!</span></h1>

  <p class="message">Tired of roofers knocking on your doors?<br>contact us because we value your time<br>as much as you value the roof over your head.</p>

  <h2 class="info-title">MORE INFORMATION</h2>

  <div class="contact contact-location">
    <svg viewBox="0 0 36 36"><circle cx="18" cy="18" r="18" fill="var(--ink)"/><path d="M18 8 a7 7 0 0 1 7 7 c0 5 -7 12 -7 12 s-7 -7 -7 -12 a7 7 0 0 1 7 -7 z" fill="var(--yellow)"/><circle cx="18" cy="15" r="2.8" fill="var(--ink)"/></svg>
    <span>Brookvale, GA</span>
  </div>
  <div class="contact contact-phone">
    <svg viewBox="0 0 36 36"><circle cx="18" cy="18" r="18" fill="var(--ink)"/><path d="M12.5 9.5 l3 -0.5 l2 5 l-2.2 1.6 a11 11 0 0 0 5 5 l1.6 -2.2 l5 2 l-0.5 3 a3 3 0 0 1 -3 2.4 C16 25.5 10.5 20 10.2 12.5 a3 3 0 0 1 2.3 -3 z" fill="var(--yellow)"/></svg>
    <span>877.612.OLUM</span>
  </div>
  <div class="contact contact-email">
    <svg viewBox="0 0 36 36"><circle cx="18" cy="18" r="18" fill="var(--ink)"/><rect x="9" y="12" width="18" height="12" fill="none" stroke="var(--yellow)" stroke-width="1.6"/><path d="M9 12 L18 19 L27 12 M9 24 L15.5 17.5 M27 24 L20.5 17.5" fill="none" stroke="var(--yellow)" stroke-width="1.6"/></svg>
    <span>info@olumroofing.com</span>
  </div>
</main>
</body>
</html>
```